BrightPath Dental
Web Presence
BrightPath Dental - Information Technology
Creative Brief
Information Technology
www.brightpathdental-demo.com
Brightpath Dental provides a wide variety of high tech dental solutions at a competitive price. We pride ourselves on the extremely high level and speed of service that we provide to our clientele. We are a local computer company that specializes in bringing our clientele the best dental technology solutions available. By allowing us to correctly integrate the right dental technology solutions, it gives your practice a technological competitive edge, increases production, and significantly enhances your patient’s experience. We provide a full array of computer services for both small and large practices. Our team services PC's and networks, digital x-ray / imaging equipment, we also provide software & hardware sales, service, upgrades, and installations, as well as data storage and backup solutions. We also provide ongoing technical support to keep you comfortable with changing technologies and ensure your practice productivity.
would like CMS designed website for either joomla or wordpress. We need the wording and the design -- we are a Lumoverde Reseller and Installer so please check out their site listed below. our logo is available: http://orders.markcraftstudio-demo.com/contests/business-logo-brightpathdental
left side
http://www.lumoverdedental-demo.com/us_region/index.aspx
http://www.qwbadvisors-demo.com/articles
http://www.orb-sys-demo.com/index.html
Additional Sites that do similar work: http://www.mnzerodental-demo.com/dataprotection.htm http://www.fenwro-demo.com/customer_care.html http://www.glimvo-demo.com/ http://www.mnzerodental-demo.com/dataprotection.htm

```html
<!DOCTYPE html>
<html lang="en">
<head>
<meta charset="utf-8">
<title>BrightPath Dental</title>
<link href="https://fonts.googleapis.com/css2?family=Arimo:wght@400;700&family=Tinos:wght@400;700&display=swap" rel="stylesheet">
<style>
:root{
  --navy:#1d3f73;
  --nav-dark:#333538;
  --nav-light:#5a5c60;
  --blue:#1a8fd8;
  --blue-deep:#0d6fb8;
  --link-blue:#1b5fa8;
  --red:#e3262b;
  --red-dark:#b9161b;
  --gold:#f3d21d;
  --text-grey:#8a8d91;
  --line-grey:#d9dcdf;
  --white:#ffffff;
}
*{box-sizing:border-box;margin:0;padding:0}
html,body{width:1200px;height:924px;overflow:hidden;background:var(--white);font-family:"Arimo",Arial,sans-serif}
.page{position:relative;width:1200px;height:924px}
.abs{position:absolute}

/* header */
.brand{left:160px;top:30px;display:flex;align-items:center;gap:12px}
.brand-dot{width:34px;height:34px;border-radius:50%;background:var(--red)}
.brand-name{font-size:28px;font-weight:700;color:var(--navy);letter-spacing:.5px}
.search{left:762px;top:42px;display:flex;align-items:center;gap:12px;font-size:15px;color:#666}
.search-field{width:140px;height:16px;background:#e6e7e8;border:1px solid #d0d2d4}

/* main nav */
.main-nav{left:155px;top:95px;width:870px;height:28px;background:linear-gradient(#55575b,#2f3134);display:flex}
.main-nav a{flex:1;color:var(--white);text-decoration:none;font-size:14px;text-align:center;line-height:28px}

/* hero */
.hero{left:155px;top:126px;width:608px;height:350px;overflow:hidden;background:linear-gradient(120deg,#e9f1f7 0%,#c9dcea 35%,#f2c7cf 60%,#b9cfe0 100%)}
.hero-arrow{width:34px;height:34px;background:#222;top:153px}
.hero-caption{left:12px;top:272px;width:530px;height:62px;background:rgba(40,40,40,.72);padding:6px 10px;overflow:hidden}
.hero-caption h2{font-family:"Tinos","Times New Roman",serif;font-weight:400;color:var(--gold);font-size:17px;line-height:20px;white-space:nowrap}
.hero-caption p{font-size:8px;color:#ddd;margin-top:5px;line-height:10px}

.thumb{top:482px;width:190px;height:96px;background:linear-gradient(135deg,#f4f8fb,#bcd6ea 55%,#e8eef3);border:3px solid var(--white);box-shadow:0 0 2px #bbb}

/* sidebar */
.sidebar{left:768px;top:125px;width:257px;height:463px;background:linear-gradient(#e9f2fa,#c7e0f4 80%,#b5d6f0)}
.contact{left:0;top:0;width:257px;height:215px;background:linear-gradient(var(--blue),var(--blue-deep))}
.contact h3{position:absolute;left:15px;top:14px;color:var(--white);font-size:22px;font-weight:400}
.field-label{position:absolute;left:15px;color:var(--white);font-size:10px}
.field{position:absolute;left:15px;width:135px;height:10px;background:var(--white)}
.send{position:absolute;left:22px;top:185px;width:52px;height:16px;background:var(--red);color:var(--white);font-size:9px;font-weight:700;text-align:center;line-height:16px}
.video-title{left:15px;top:245px;font-size:19px;color:#333}
.video{left:15px;width:230px;display:flex;gap:10px}
.video-thumb{width:60px;height:62px;background:#3a3c40;display:flex;align-items:center;justify-content:center;flex:none}
.video h4{font-size:9px;color:var(--link-blue);font-weight:700}
.video p{font-size:8px;color:#555;line-height:10px;margin-top:2px}
.read-more{left:115px;top:437px;background:var(--red);color:var(--white);font-size:8px;font-weight:700;padding:3px 6px}

/* columns */
.feature{top:616px;width:255px}
.feature h3{font-family:"Tinos","Times New Roman",serif;font-size:13px;font-weight:700;color:var(--link-blue)}
.feature p{font-family:"Tinos","Times New Roman",serif;font-size:10.5px;line-height:13px;color:var(--text-grey);margin-top:14px}
.more{top:748px;width:22px;height:9px;background:var(--link-blue)}

/* footer */
.contact-band{left:0;top:793px;width:1200px;height:70px;background:linear-gradient(var(--red),var(--red-dark));color:var(--white);text-align:center;font-size:10px}
.contact-band p{margin-top:18px}
.contact-band p + p{margin-top:10px}
.footer-nav{left:0;top:866px;width:1200px;height:58px;background:linear-gradient(#3a3c40,#1f2022)}
.footer-nav a{position:absolute;top:22px;color:var(--white);font-size:11px;text-decoration:none}
</style>
</head>
<body>
<div class="page">

  <header>
    <div class="abs brand"><span class="brand-dot"></span><span class="brand-name">BrightPath Dental</span></div>
    <div class="abs search">Search: <span class="search-field"></span>
      <svg width="22" height="22" viewBox="0 0 22 22"><circle cx="9" cy="9" r="6.5" fill="none" stroke="#666" stroke-width="2"/><line x1="14" y1="14" x2="20" y2="20" stroke="#666" stroke-width="2.5"/></svg>
    </div>
    <nav class="abs main-nav">
      <a href="#">Home</a><a href="#">About Us</a><a href="#">Services</a><a href="#">Order</a><a href="#">Affiliates</a><a href="#">Contacts</a>
    </nav>
  </header>

  <section class="abs hero" role="img" aria-label="Photo of a dentist treating a young patient in a dental chair">
    <div class="abs hero-arrow" style="left:20px">
      <svg width="34" height="34" viewBox="0 0 34 34"><path d="M21 9 L12 17 L21 25 Z" fill="#fff"/></svg>
    </div>
    <div class="abs hero-arrow" style="left:558px">
      <svg width="34" height="34" viewBox="0 0 34 34"><path d="M13 9 L22 17 L13 25 Z" fill="#fff"/></svg>
    </div>
    <div class="abs hero-caption">
      <h2>Brightpath Dental provides a wide variety of high tech dental solutions</h2>
      <p>Brightpath Dental provides a wide variety of high tech dental solutions at a fair price. We pride ourselves on the high level and speed of service we provide.</p>
    </div>
  </section>

  <div class="abs thumb" style="left:157px" role="img" aria-label="Photo of dental imaging equipment"></div>
  <div class="abs thumb" style="left:369px" role="img" aria-label="Photo of a smiling patient in the dental chair"></div>
  <div class="abs thumb" style="left:572px" role="img" aria-label="Photo of a dental team at work"></div>

  <aside class="abs sidebar">
    <div class="abs contact">
      <h3>Contact Form</h3>
      <span class="field-label" style="top:51px">Name</span><span class="field" style="top:65px"></span>
      <span class="field-label" style="top:87px">Email</span><span class="field" style="top:101px"></span>
      <span class="field-label" style="top:123px">Comment</span><span class="field" style="top:137px;height:32px;width:170px"></span>
      <span class="send">SEND</span>
    </div>
    <div class="abs video-title">Popular Video</div>
    <div class="abs video" style="top:280px">
      <div class="video-thumb"><svg width="18" height="18" viewBox="0 0 18 18"><path d="M4 2 L15 9 L4 16 Z" fill="#ddd"/></svg></div>
      <div><h4>Egesum Imprids</h4><p>Short clip on digital x-ray setup and daily imaging workflow.</p></div>
    </div>
    <div class="abs video" style="top:367px">
      <div class="video-thumb"><svg width="18" height="18" viewBox="0 0 18 18"><path d="M4 2 L15 9 L4 16 Z" fill="#ddd"/></svg></div>
      <div><h4>Egesum Imprids</h4><p>Short clip on data backup plans for busy dental offices.</p></div>
    </div>
    <span class="abs read-more">READ MORE</span>
  </aside>

  <main>
    <article class="abs feature" style="left:162px">
      <h3>Orthodontic, OMS and Endodontic Systems</h3>
      <p>At Glimvo-demo.com we design, install and support custom, specialty driven, digital network systems. Be whether you're a General Dentist, Orthodontist, Oral Surgeon, Endodontist or Periodontist, our technology is customized for you, your patients and to increase staff efficiency. Each system is customized to your practice's needs.</p>
    </article>
    <span class="abs more" style="left:372px"></span>
    <article class="abs feature" style="left:458px">
      <h3>Orthodontic, OMS and Endodontic Systems</h3>
      <p>At Glimvo-demo.com we design, install and support custom, specialty driven, digital network systems. Be whether you're a General Dentist, Orthodontist, Oral Surgeon, Endodontist or Periodontist, our technology is customized for you, your patients and to increase staff efficiency. Each system is customized to your practice's needs.</p>
    </article>
    <span class="abs more" style="left:668px"></span>
    <article class="abs feature" style="left:752px">
      <h3>Orthodontic, OMS and Endodontic Systems</h3>
      <p>At Glimvo-demo.com we design, install and support custom, specialty driven, digital network systems. Be whether you're a General Dentist, Orthodontist, Oral Surgeon, Endodontist or Periodontist, our technology is customized for you, your patients and to increase staff efficiency. Each system is customized to your practice's needs.</p>
    </article>
    <span class="abs more" style="left:962px"></span>
  </main>

  <footer>
    <div class="abs contact-band">
      <p>T: (555) 201-4410 &bull; T: (555) 203-7712 &bull; E: info@brightpathdental-demo.com</p>
      <p>Support T: (555) 208-3340 option 3 &bull; E: support@brightpathdental-demo.com &nbsp; Sales T: (555) 208-3340 option 1 &bull; E: sales@brightpathdental-demo.com</p>
    </div>
    <nav class="abs footer-nav">
      <a href="#" style="left:188px">Home</a>
      <a href="#" style="left:265px">Specialities</a>
      <a href="#" style="left:348px">Dental System</a>
      <a href="#" style="left:440px">Our Partners</a>
      <a href="#" style="left:535px">Careers</a>
      <a href="#" style="left:622px">Contact Us</a>
    </nav>
  </footer>

</div>
</body>
</html>
```